Halvern - Energy management company website design

We are interested in a total redesign of our website at www.halvernpowerco.co.uk. We are happy with our current colour scheme and logo but are ready for a new website.

The site is running on a CMS called Umbraco and will remain on this CMS. We are just looking for the html/css and js files so I can build the templates.

We are looking for a home page and maybe a couple of different types of content page. We would like the site to look clean and professional but not necessarily like every other corporate website.
We are really open to any design ideas, we've left the brief quite ambiguous for that reason. We are happy to consider any design no matter how unorthodox as long as it remains professional.

Target Market(s)

Large Businesses

Industry/Entity Type

It Company

Coding

Coded - Design and coding required

Number of Pages Required

3 page

Font styles to use
Sans Serif

Requirements
Must have
• We need a landing page designed and possibly two different kinds of content page allowing for different styles of content. We will want the css and js code with the pages.
• On the home page we would like Two prominent articles/products.
• Then a selection of our other products/services.
• Testimonials, Case studies and News Articles.
• Company colours:
• Text and topleft arrow blue (dark):
• R: 0 G: 96 B: 167
• Red Text and Arrow:
• R: 237 G: 27 B: 35
• Bottom left arrow blue (medium):
• R: 0 G: 174 B: 239
• Bottom right arrow blue (light):
• R: 171 G: 225 B: 250
Nice to have
• We are open to a potentially radical redesign of the site, it doesn't necessarily need to look like every other corporate website.
• We would like to see one or two designs base on this type of imagery:
• http://lnkbox.example/Qa7rTe
• http://lnkbox.example/Mv3pLd
• http://lnkbox.example/Xk9wBn

```html
<!DOCTYPE html>
<html lang="en">
<head>
<meta charset="utf-8">
<title>Halvern – Integrated Energy Experts</title>
<link rel="stylesheet" href="https://fonts.googleapis.com/css2?family=Open+Sans:ital,wght@0,400;0,600;0,700;0,800;1,400;1,600;1,700&display=swap">
<style>
:root{
  --blue-dark:#0060a7;
  --blue-mid:#00aeef;
  --blue-light:#abe1fa;
  --red:#ed1b23;
  --ink:#333333;
  --ink-soft:#555555;
  --nav-ink:#0a4f8c;
  --rule:#cfcfcf;
  --panel:#f7f7f7;
  --map:#ebebeb;
  --footer:#3b3b3b;
  --footer-ink:#8a8a8a;
  --white:#ffffff;
}
*{box-sizing:border-box;margin:0;padding:0}
html,body{width:1200px;height:2483px;overflow:hidden;background:var(--white)}
body{position:relative;font-family:"Open Sans",Arial,sans-serif;color:var(--ink)}

/* header */
.site-header{position:absolute;left:0;top:0;width:1200px;height:108px;background:var(--white)}
.brand{position:absolute;display:flex;align-items:center;gap:10px;font-weight:700;font-size:38px;letter-spacing:-0.5px}
.brand-mark{width:40px;height:40px;border-radius:50%;border:5px solid currentColor}
.site-header .brand{left:71px;top:24px;color:var(--blue-dark)}
.main-nav{position:absolute;left:482px;top:41px;height:30px;font-size:15px;color:var(--nav-ink)}
.main-nav a{color:inherit;text-decoration:none;line-height:30px;position:absolute;top:0;white-space:nowrap}
.main-nav .is-active{background:var(--blue-dark);color:var(--white);width:97px;text-align:center}

/* hero */
.hero{position:absolute;left:0;top:108px;width:1200px;height:430px;background:linear-gradient(100deg,#8cc6ee 0%,#a9d6f3 35%,#6fb3e6 60%,#9bcdf0 100%)}
.hero-title{position:absolute;left:132px;top:40px;font-weight:800;font-size:42px;line-height:48px;color:var(--white);text-transform:uppercase}
.hero-title .accent{color:var(--blue-dark)}
.hero-text{position:absolute;left:132px;top:245px;width:330px;font-size:10.5px;line-height:15px;color:var(--blue-dark)}
.btn-ghost{position:absolute;left:132px;top:331px;width:194px;height:51px;border:2px solid rgba(255,255,255,.8);color:var(--white);font-size:16px;text-align:center;line-height:47px;text-transform:uppercase}

/* esos */
.esos{position:absolute;left:0;top:538px;width:1200px;height:369px;background:var(--panel);border-bottom:2px solid var(--rule)}
.esos-title{position:absolute;left:132px;top:72px;font-weight:800;font-size:36px;line-height:40px;color:var(--blue-mid)}
.esos-sub{position:absolute;left:132px;top:158px;font-size:10.5px;line-height:15px;font-style:italic;font-weight:600;color:var(--blue-dark);text-transform:uppercase}
.esos-intro{position:absolute;left:132px;top:198px;width:285px;font-size:11px;line-height:17px;color:var(--ink)}
.btn-outline{position:absolute;border:1.5px solid #8d8d8d;background:var(--white);color:var(--ink);font-size:13px;text-align:center;text-transform:uppercase}
.esos .btn-outline{left:132px;top:276px;width:144px;height:40px;line-height:37px}
.esos-leaflet{position:absolute;left:386px;top:74px;width:172px;height:242px;background:linear-gradient(180deg,#ffffff 0%,#fdf0f0 55%,#ffffff 100%);border:1px solid #d9d9d9;box-shadow:0 2px 5px rgba(0,0,0,.25)}
.esos-body{position:absolute;left:601px;top:82px;width:466px;font-size:12.5px;line-height:24px;color:var(--ink-soft);text-align:justify}
.esos-body strong{font-weight:400;font-size:16px;color:var(--ink)}

/* services */
.section-title{position:absolute;left:0;width:1200px;text-align:center;font-weight:700;font-size:26px;color:#555}
.section-title .line{display:inline-block;width:58px;height:3px;background:#9a9a9a;vertical-align:middle;margin:0 8px}
.services .section-title{top:948px}
.service{position:absolute;top:1016px;width:213px}
.service-photo{width:213px;height:129px;border:1px solid #cfcfcf}
.service-name{margin-top:20px;font-size:15px;font-weight:400;color:#444;text-transform:uppercase}
.service-text{margin-top:2px;font-size:13px;line-height:21px;color:var(--ink)}
.read-more{font-size:12px;color:var(--ink);display:flex;align-items:center;gap:6px}
.service .read-more{position:absolute;top:240px;right:12px}

/* testimonials */
.testimonials{position:absolute;left:0;top:1337px;width:1200px;height:310px;background:var(--map)}
.testimonials .section-title{top:38px;font-weight:400;font-size:28px;line-height:34px;color:#555}
.testimonials .section-title b{font-weight:700}
.avatar{position:absolute;left:202px;top:119px;width:96px;height:96px;border-radius:50%;border:4px solid var(--white);background:linear-gradient(180deg,#cfd3d8,#9aa3ad)}
.quote{position:absolute;left:323px;top:76px;width:678px;font-size:13.5px;line-height:26px;color:#555}
.quote-by{position:absolute;right:202px;top:218px;text-align:right;font-size:12.5px;line-height:24px;font-style:italic;font-weight:700;color:#555}
.dots{position:absolute;left:322px;top:249px;display:flex;gap:3px}
.dots span{width:11px;height:11px;border-radius:50%;border:2px solid #777}
.dots span:first-child{background:#777}

/* news & case study */
.block-title{position:absolute;top:1690px;font-size:21px;font-weight:400;color:#333;text-transform:uppercase}
.news-text{position:absolute;left:159px;top:1737px;width:260px;font-size:11.8px;line-height:22.5px;text-align:justify;color:var(--ink)}
.news-date{position:absolute;left:159px;top:1878px;width:260px;text-align:right;font-size:12px;font-style:italic;font-weight:700;color:#444}
.expertise{position:absolute;left:520px;top:1728px;width:160px;text-align:center;color:var(--blue-dark)}
.expertise-num{font-weight:800;font-size:62px;line-height:64px;letter-spacing:-2px}
.expertise-word{font-weight:700;font-size:22px;line-height:24px}
.expertise-text{position:absolute;left:470px;top:1831px;width:260px;text-align:center;font-size:12px;color:var(--ink)}
.news .btn-outline{left:528px;top:1870px;width:144px;height:37px;line-height:34px}
.case-sub{position:absolute;left:775px;top:1737px;font-size:14.5px;font-weight:700;color:#333}
.case-text{position:absolute;left:775px;top:1760px;width:302px;font-size:11.8px;line-height:22.5px;text-align:justify;color:var(--ink)}
.case-more{position:absolute;left:777px;top:1877px}
.case-more b{font-weight:700}

/* clients */
.clients{position:absolute;left:0;top:1970px;width:1200px;height:135px;border-top:2px solid #d8d8d8}
.client{position:absolute;top:41px;width:145px;height:53px;border:1px solid #cfcfcf;display:flex;align-items:center;justify-content:center;font-size:15px;font-weight:600;color:#444}
.slider-arrow{position:absolute;top:50px}

/* footer */
.site-footer{position:absolute;left:0;top:2105px;width:1200px;height:378px;background:var(--footer);color:var(--footer-ink)}
.site-footer .brand{left:74px;top:44px;color:#bdbdbd}
.address{position:absolute;left:82px;top:132px;font-size:12px;line-height:16.5px;font-weight:600;color:#8a8a8a}
.social{position:absolute;left:82px;top:236px;display:flex;gap:5px}
.social span{width:18px;height:18px;background:#8a8a8a}
.footer-col{position:absolute;top:62px}
.footer-col h3{font-size:14.5px;font-weight:700;color:var(--white);text-transform:uppercase;margin-bottom:44px}
.footer-col li{list-style:none;font-size:12px;line-height:22px;font-weight:600;color:#7c7c7c}
.photo-title{position:absolute;left:889px;top:62px;width:245px;padding-bottom:14px;border-bottom:1px solid #555;font-size:14.5px;font-weight:700;color:var(--white)}
.photo-grid{position:absolute;left:889px;top:133px;display:grid;grid-template-columns:repeat(3,78px);grid-template-rows:repeat(2,75px);gap:5px}
.photo-grid div{width:78px;height:75px}
.copyright{position:absolute;left:0;top:314px;width:1200px;text-align:center;font-size:12px;color:#8a8a8a}
</style>
</head>
<body>

<header class="site-header">
  <div class="brand"><span class="brand-mark"></span>Halvern</div>
  <nav class="main-nav">
    <a class="is-active" style="left:0">HOME</a>
    <a style="left:116px">SERICES</a>
    <a style="left:215px">CUSTOMERS</a>
    <a style="left:347px">PULSE</a>
    <a style="left:436px">COMPANY</a>
    <a style="left:552px">CONTACT US</a>
  </nav>
</header>

<section class="hero" role="img" aria-label="Hands holding a glowing blue glass globe">
  <h1 class="hero-title"><span class="accent">Uncovering</span><br>The underlying<br>cost<br>of energy</h1>
  <p class="hero-text">Lorem ipsum dolor sit amet, quis deseruisse usu ea. Ut ubique tempor duo, ne autem interesset complectitur has. Ut est aeque labore luptatum, ei qui purto appetere detraxit. Purto nemore dissentiet ne mel, no delenit aperiian vituperata pro, ei partem.</p>
  <div class="btn-ghost">Know more</div>
</section>

<section class="esos">
  <h2 class="esos-title">WHAT<br>IS ESOS ?</h2>
  <p class="esos-sub">ESOS is the eportunity scheme,<br>a piece of European legis is now UK law.</p>
  <p class="esos-intro">ESOS energy audits are designed to help large improve their energy efficiency – and reduce costs.</p>
  <div class="btn-outline">Know more</div>
  <div class="esos-leaflet" role="img" aria-label="Leaflet cover titled What is ESOS with four numbered steps"></div>
  <div class="esos-body">
    <p><strong>ESOS</strong> (Energy Savings Opportunity Scheme) presents a new and significant opportunity for large UK businesses. UK Government predicts that ESOS could help deliver savings of nearly £2bn.A PIECE OF EUROPEAN LEGSLATION THAT IS NOW UK LAW.</p>
    <p>ESOS is a new piece of EU legislation which requires member states to introduce a mandatory programme of energy audits for 'large enterprises'. This means over 9000 of Britain's biggest companies will be required to comply - with the initial audits to be undertaken by 5th December 2015.</p>
  </div>
</section>

<section class="services">
  <h2 class="section-title"><span class="line"></span>ENERGY SERVICES<span class="line"></span></h2>
  <article class="service" style="left:129px">
    <div class="service-photo" role="img" aria-label="Hand drawing arrows for cost, quality and efficiency" style="background:linear-gradient(135deg,#f4f4f4,#e2e6e2)"></div>
    <h3 class="service-name">Efficiency</h3>
    <p class="service-text">Lorem ipsum dolor sit amet, verear aperiri antiopam nec cu, no oratio omnium</p>
    <span class="read-more">Read more <svg width="6" height="10" viewBox="0 0 6 10"><path d="M1 1l4 4-4 4" fill="none" stroke="#333" stroke-width="1.5"/></svg></span>
  </article>
  <article class="service" style="left:370px">
    <div class="service-photo" role="img" aria-label="Hands holding a classic bulb and an energy-saving bulb" style="background:linear-gradient(135deg,#7c8f98,#dfe6ea)"></div>
    <h3 class="service-name">Complience</h3>
    <p class="service-text">Lorem ipsum dolor sit amet, verear aperiri antiopam nec cu, no oratio omnium</p>
    <span class="read-more">Read more <svg width="6" height="10" viewBox="0 0 6 10"><path d="M1 1l4 4-4 4" fill="none" stroke="#333" stroke-width="1.5"/></svg></span>
  </article>
  <article class="service" style="left:612px">
    <div class="service-photo" role="img" aria-label="Businessman with a glowing data chart" style="background:linear-gradient(135deg,#1c2a3e,#5a7aa0)"></div>
    <h3 class="service-name">Analisis</h3>
    <p class="service-text">Lorem ipsum dolor sit amet, verear aperiri antiopam nec cu, no oratio omnium</p>
    <span class="read-more">Read more <svg width="6" height="10" viewBox="0 0 6 10"><path d="M1 1l4 4-4 4" fill="none" stroke="#333" stroke-width="1.5"/></svg></span>
  </article>
  <article class="service" style="left:853px">
    <div class="service-photo" role="img" aria-label="Robot hand shaking a human hand" style="background:linear-gradient(135deg,#ffffff,#ece7e2)"></div>
    <h3 class="service-name">Procurement</h3>
    <p class="service-text">Lorem ipsum dolor sit amet, verear aperiri antiopam nec cu, no oratio omnium</p>
    <span class="read-more">Read more <svg width="6" height="10" viewBox="0 0 6 10"><path d="M1 1l4 4-4 4" fill="none" stroke="#333" stroke-width="1.5"/></svg></span>
  </article>
</section>

<section class="testimonials" role="region" aria-label="Customer testimonials over a faint road map background">
  <h2 class="section-title">Customer <b>TESTIMONIALS</b></h2>
  <div class="avatar" role="img" aria-label="Customer portrait"></div>
  <p class="quote">Lorem ipsum dolor sit amet, quis deseruisse usu ea. plecppetere detraxit. Purto nemore dissentiet ne mel, no delenit aperiian vituperata pro, ei partem detraxit honestatis quo. Eam ea aLorem ipsum dolor sit amet, quis deseruisse usu ea. plecppetere detraxit. Purto nemore dissentiet ne mel, no delenit aperiian vituperata pro, ei partem detraxit honestatis quo. Eam ea a</p>
  <p class="quote-by">Daniel Pryce<br>CEO of Norbeck Enterprises</p>
  <div class="dots"><span></span><span></span><span></span></div>
</section>

<section class="news">
  <h2 class="block-title" style="left:157px">Latest news</h2>
  <p class="news-text">Lorem ipsum dolor sit amet, quis deseruisse usu ea Ut ubique tempor duo, ne autem intertiet, debitis abhorreant eam an, at esse petentium sed. Lorem ipsum dolor sit amet, quis deseruisse usu ea Ut ubique tempor duo, ne autem interesset complecitur isabho</p>
  <p class="news-date">09.jan.16</p>
  <div class="expertise"><div class="expertise-num">360</div><div class="expertise-word">EXPERTISE</div></div>
  <p class="expertise-text">Lorem ipsum dolor sit amet, quis dese-</p>
  <div class="btn-outline">Know more</div>

  <h2 class="block-title" style="left:775px">Case study</h2>
  <h3 class="case-sub">A decade of savings</h3>
  <p class="case-text">Lorem ipsum dolor sit amet, quis deseruisse usu ea. Ut ubique tempor duo, ne autem interesset complectitur has. Ut est aeque labore luptatum, ei qui purto appetere detraxit. Purto nemore ei qui purto appetere</p>
  <span class="read-more case-more"><b>Read more</b> <svg width="6" height="10" viewBox="0 0 6 10"><path d="M1 1l4 4-4 4" fill="none" stroke="#333" stroke-width="1.5"/></svg></span>
</section>

<section class="clients">
  <svg class="slider-arrow" style="left:98px" width="20" height="34" viewBox="0 0 20 34"><path d="M16 3L4 17l12 14" fill="none" stroke="#b5b5b5" stroke-width="5"/></svg>
  <div class="client" style="left:136px">Velmar</div>
  <div class="client" style="left:293px">Corrow Airport</div>
  <div class="client" style="left:452px">Dunlane</div>
  <div class="client" style="left:614px">Ashby Tate</div>
  <div class="client" style="left:766px">Penfold</div>
  <div class="client" style="left:925px">Marsh Lane</div>
  <svg class="slider-arrow" style="left:1082px" width="20" height="34" viewBox="0 0 20 34"><path d="M4 3l12 14L4 31" fill="none" stroke="#b5b5b5" stroke-width="5"/></svg>
</section>

<footer class="site-footer">
  <div class="brand"><span class="brand-mark"></span>Halvern</div>
  <p class="address">Halvern House<br>Oakmoor Drive<br>Oakmoor Business Park<br>Brackton<br>BK4 2QE</p>
  <div class="social"><span></span><span></span><span></span><span></span><span></span><span></span></div>
  <div class="footer-col" style="left:349px">
    <h3>Additional links</h3>
    <ul><li>Creative I Ideas</li><li>Company Analysis</li><li>Brand Creation</li><li>Corporate Identity</li><li>Press Inquiries</li><li>Product Details</li></ul>
  </div>
  <div class="footer-col" style="left:617px">
    <h3>Useful links</h3>
    <ul><li>Creative I Ideas</li><li>Company Analysis</li><li>Brand Creation</li><li>Corporate Identity</li><li>Press Inquiries</li><li>Product Details</li></ul>
  </div>
  <h3 class="photo-title">PHOTO STREAM</h3>
  <div class="photo-grid">
    <div role="img" aria-label="Black and white street photo" style="background:linear-gradient(135deg,#333,#bbb)"></div>
    <div role="img" aria-label="Colourful art wall" style="background:linear-gradient(135deg,#c0392b,#2e6fb5)"></div>
    <div role="img" aria-label="Quiet lane" style="background:linear-gradient(135deg,#a9b8c4,#7a8670)"></div>
    <div role="img" aria-label="Blue shop front" style="background:linear-gradient(135deg,#1d6fa8,#0f2f4a)"></div>
    <div role="img" aria-label="Autumn tree" style="background:linear-gradient(135deg,#5d4a1c,#c99a2e)"></div>
    <div role="img" aria-label="Golden autumn leaves" style="background:linear-gradient(135deg,#e0b432,#6b5a22)"></div>
  </div>
  <p class="copyright">Copyright (c) 2015 -16 tesselworks</p>
</footer>

</body>
</html>
```